lunch and dinne(al a carte) menus

we are a medium sized licenced club that has taken back the dining in the club
in the western suburbs of sydney working class with a rugby league base
our logo is a wolf kelford hawks

Reason: We have changed the name to Bluegate grill it could be done as Bluegate or Bluegate or Bluegate We need a lunch menu and a seperate dinner menu eg Bluegate grill l u n c h or Bluegate grill d i n n e r

Reason: Weve changed the name

Target Market(s)

young families, working class rugby leagues sporty types

Industry/Entity Type

Club

Requirements
Must have
• user friendly

```html
<!DOCTYPE html>
<html lang="en">
<head>
<meta charset="utf-8">
<title>Kelford Hawks Char Grill Menu</title>
<link href="https://fonts.googleapis.com/css2?family=Carlito:ital,wght@0,400;0,700;1,400&family=Lora:ital,wght@1,600&family=Open+Sans:ital,wght@0,300;0,400;0,600;0,700;1,400&display=swap" rel="stylesheet">
<style>
:root{
  --paper:#ffffff;
  --green:#3a8a1f;
  --green-deep:#2d7a16;
  --sun:#f6e24a;
  --sun-soft:#fbf5c0;
  --lime:#c9df5a;
  --gold:#f2a93b;
  --ink:#1a1a1a;
  --ink-soft:#2c2c2c;
  --white:#ffffff;
}
*{margin:0;padding:0;box-sizing:border-box}
html,body{width:1200px;height:900px;overflow:hidden;background:var(--paper)}
.canvas{position:relative;width:1200px;height:900px;background:var(--paper);color:var(--ink);font-family:"Carlito",sans-serif}
.page{position:absolute;top:42px;width:588px;height:817px;overflow:hidden;
  background:
    linear-gradient(180deg,rgba(255,255,255,0) 0%,rgba(255,255,255,0) 74%,rgba(92,168,48,.85) 88%,var(--green-deep) 100%),
    radial-gradient(ellipse 95% 80% at 50% 22%,var(--white) 0%,var(--sun-soft) 28%,var(--sun) 55%,var(--lime) 82%,#8fc23a 100%);}
.page-left{left:7px}
.page-right{left:600px}
.title-bar{position:absolute;top:45px;height:32px;background:var(--green);color:var(--white);
  font-family:"Open Sans",sans-serif;font-weight:400;font-size:26px;letter-spacing:1px;line-height:32px;padding-left:20px}
.brand{position:absolute;top:42px;width:205px;text-align:center;font-family:"Open Sans",sans-serif;font-weight:700;font-size:26px;line-height:30px;color:var(--green-deep)}
.brand-mark{display:inline-block;width:14px;height:14px;border-radius:50%;background:var(--gold);margin-right:6px}
.since{position:absolute;top:108px;width:200px;text-align:center;font-family:"Lora",serif;font-style:italic;font-weight:600;font-size:13px;color:var(--ink)}
.since::before,.since::after{content:"";display:inline-block;width:42px;height:1px;background:var(--ink);vertical-align:middle;margin:0 8px}
.abs{position:absolute;white-space:nowrap}
.col-head{font-size:8px;color:var(--ink-soft);letter-spacing:.3px}
.snack{font-size:10px;font-weight:700}
.snack-sub{font-size:9.5px;font-style:italic;font-weight:400}
.price{font-size:10px}
.kids-title{font-size:12px;font-weight:700}
.kids{font-size:9.5px}
.right{font-family:"Open Sans",sans-serif}
.sec{font-size:12.5px;font-weight:700;letter-spacing:1.5px;text-align:center}
.dish{font-size:9.5px;font-weight:600;letter-spacing:1px}
.dprice{font-size:9.5px;letter-spacing:.5px}
.desc{position:absolute;white-space:nowrap;text-align:center;font-size:9.5px;font-style:italic;letter-spacing:.9px;line-height:13px;color:var(--ink)}
.desc-l{left:603px;width:300px}
.desc-r{left:895px;width:300px}
.footnote{font-family:"Open Sans",sans-serif;font-size:9px;font-weight:600;letter-spacing:1.2px;color:var(--white)}
</style>
</head>
<body>
<div class="canvas">
  <div class="page page-left"></div>
  <div class="page page-right"></div>

  <div class="title-bar" style="left:7px;width:363px">CHAR GRILL MENU</div>
  <div class="brand" style="left:380px"><span class="brand-mark"></span>KELFORD HAWKS</div>
  <div class="since" style="left:385px">Since 1912</div>

  <div class="abs col-head" style="left:208px;top:145px">MEMBER</div>
  <div class="abs col-head" style="left:268px;top:145px">VISITOR</div>
  <div class="abs col-head" style="left:498px;top:145px">MEMBER</div>
  <div class="abs col-head" style="left:558px;top:145px">VISITOR</div>

  <div class="abs snack" style="left:28px;top:156px">4 Vegetarian Spring Rolls</div><div class="abs price" style="left:222px;top:156px">$8</div><div class="abs price" style="left:276px;top:156px">$10</div>
  <div class="abs snack-sub" style="left:38px;top:169px">with Rice</div>
  <div class="abs snack" style="left:28px;top:187px">Club Sandwich</div><div class="abs price" style="left:222px;top:187px">$8</div><div class="abs price" style="left:276px;top:187px">$10</div>
  <div class="abs snack-sub" style="left:38px;top:200px">with Chips</div>
  <div class="abs snack-sub" style="left:38px;top:212px;font-style:normal">(chicken, bacon, cheese, tomato, lettuce &amp; mayo)</div>
  <div class="abs snack" style="left:28px;top:233px">Home Made Quiche with Chips</div><div class="abs price" style="left:222px;top:233px">$8</div><div class="abs price" style="left:276px;top:233px">$10</div>
  <div class="abs snack" style="left:28px;top:259px">T-Bone with Chips &amp; Salad</div><div class="abs price" style="left:222px;top:259px">$10</div><div class="abs price" style="left:276px;top:259px">$12</div>
  <div class="abs snack" style="left:28px;top:278px">Open Hamburger</div><div class="abs price" style="left:222px;top:278px">$10</div><div class="abs price" style="left:276px;top:278px">$12</div>
  <div class="abs snack-sub" style="left:38px;top:291px">with the Works &amp; Chips</div>
  <div class="abs snack" style="left:28px;top:310px">Cajun Chicken Burger</div><div class="abs price" style="left:222px;top:310px">$10</div><div class="abs price" style="left:276px;top:310px">$12</div>
  <div class="abs snack-sub" style="left:38px;top:323px">with Chips</div>
  <div class="abs snack" style="left:28px;top:342px">Spaghetti Bolognaise</div><div class="abs price" style="left:222px;top:342px">$10</div><div class="abs price" style="left:276px;top:342px">$12</div>
  <div class="abs snack" style="left:28px;top:361px">Chicken Caesar Salad</div><div class="abs price" style="left:222px;top:361px">$10</div><div class="abs price" style="left:276px;top:361px">$12</div>
  <div class="abs snack" style="left:28px;top:380px">Bangers &amp; Mash</div><div class="abs price" style="left:222px;top:380px">$10</div><div class="abs price" style="left:276px;top:380px">$12</div>
  <div class="abs snack-sub" style="left:38px;top:393px">(1 thick &amp; 1 thin sausage)</div>
  <div class="abs snack" style="left:28px;top:406px">Vegetarian Lasagne</div><div class="abs price" style="left:222px;top:406px">$10</div><div class="abs price" style="left:276px;top:406px">$12</div>
  <div class="abs snack-sub" style="left:38px;top:419px">with Chips &amp; Salad</div>

  <div class="abs snack" style="left:318px;top:156px">Chicken or Veal Schnitzel</div><div class="abs price" style="left:502px;top:156px">$14</div><div class="abs price" style="left:567px;top:156px">$16</div>
  <div class="abs snack-sub" style="left:328px;top:169px">with Chips &amp; Salad</div>
  <div class="abs snack" style="left:318px;top:188px">Open Steak Sandwich</div><div class="abs price" style="left:502px;top:188px">$14</div><div class="abs price" style="left:567px;top:188px">$16</div>
  <div class="abs snack-sub" style="left:328px;top:201px">(cheese, pineapple, egg)</div>
  <div class="abs snack" style="left:318px;top:220px">All Day Breakfast</div><div class="abs price" style="left:502px;top:220px">$14</div><div class="abs price" style="left:567px;top:220px">$16</div>
  <div class="abs snack-sub" style="left:328px;top:233px">(sausage, egg, bacon, mushrooms,</div>
  <div class="abs snack-sub" style="left:328px;top:245px">tomato, hash brown &amp; toast)</div>
  <div class="abs snack" style="left:318px;top:264px">Garlic Prawns</div><div class="abs price" style="left:502px;top:264px">$14</div><div class="abs price" style="left:567px;top:264px">$16</div>
  <div class="abs snack-sub" style="left:328px;top:277px">with Rice &amp; Salad</div>
  <div class="abs snack" style="left:318px;top:298px">Beer Battered Barramundi</div><div class="abs price" style="left:502px;top:298px">$14</div><div class="abs price" style="left:567px;top:298px">$16</div>
  <div class="abs snack-sub" style="left:328px;top:311px">with Chips &amp; Salad</div>
  <div class="abs snack" style="left:318px;top:330px">Seafood Basket</div><div class="abs price" style="left:502px;top:330px">$14</div><div class="abs price" style="left:567px;top:330px">$16</div>
  <div class="abs snack-sub" style="left:328px;top:343px">with Chips &amp; Salad</div>

  <div class="abs kids-title" style="left:274px;top:491px">KIDS MENU</div>
  <div class="abs kids" style="left:100px;top:507px;font-weight:700">Sandwiches</div>
  <div class="abs kids" style="left:135px;top:520px">Savoury Spread</div>
  <div class="abs kids" style="left:238px;top:520px">Peanut Butter</div>
  <div class="abs kids" style="left:387px;top:520px">Choc Spread</div>
  <div class="abs kids" style="left:478px;top:520px">$3</div>
  <div class="abs kids" style="left:135px;top:540px">Strawberry Jam</div>
  <div class="abs kids" style="left:238px;top:540px">Devon &amp; Tomato Sauce</div>
  <div class="abs kids" style="left:100px;top:558px">Chicken Nuggets</div><div class="abs kids" style="left:478px;top:558px">$5</div>
  <div class="abs kids" style="left:110px;top:571px;font-style:italic">with Chips</div>
  <div class="abs kids" style="left:100px;top:585px">Cheese Burger</div><div class="abs kids" style="left:478px;top:585px">$5</div>
  <div class="abs kids" style="left:110px;top:598px;font-style:italic">with Chips</div>

  <div class="title-bar" style="left:600px;width:364px">CHAR GRILL MENU</div>
  <div class="brand" style="left:973px"><span class="brand-mark"></span>KELFORD HAWKS</div>
  <div class="since" style="left:978px">Since 1912</div>

  <div class="right">
    <div class="abs sec" style="left:618px;top:124px;width:270px">CHARGRILL</div>
    <div class="abs col-head" style="left:787px;top:141px;letter-spacing:1px">MEMBER</div>
    <div class="abs col-head" style="left:848px;top:141px;letter-spacing:1px">VISITOR</div>

    <div class="abs dish" style="left:618px;top:153px">MADCOW</div><div class="abs dprice" style="left:797px;top:153px">$ 28</div><div class="abs dprice" style="left:865px;top:153px">$30</div>
    <div class="desc desc-l" style="top:167px">A large tender rump topped with bug tail meat<br>calamari, scallops, prawns &amp; mussels.<br>All in a garlic white sauce</div>

    <div class="abs dish" style="left:618px;top:214px">BBQ</div><div class="abs dprice" style="left:797px;top:214px">$ 28</div><div class="abs dprice" style="left:865px;top:214px">$30</div>
    <div class="desc desc-l" style="top:228px">Massive rump steak cooked the way God intend-<br>ed it, with bacon melted cheddar, onion rings,<br>corn kernels and beetroot finished with a dollop<br>of sour cream</div>

    <div class="abs dish" style="left:618px;top:289px">CLUB SPECIAL</div><div class="abs dprice" style="left:797px;top:289px">$ 28</div><div class="abs dprice" style="left:865px;top:289px">$30</div>
    <div class="desc desc-l" style="top:303px">Scotch fillet steak cooked with love, topped with<br>fried bacon fanned avocado &amp; melted camembert<br>cheese with the sauce of your choice</div>

    <div class="abs dish" style="left:618px;top:350px">SURF &amp; TURF</div><div class="abs dprice" style="left:797px;top:350px">$ 28</div><div class="abs dprice" style="left:865px;top:350px">$30</div>
    <div class="desc desc-l" style="top:364px">Tender scotch fillet steak topped with large tiger<br>prawns in a creamy garlic sauce</div>

    <div class="abs dish" style="left:618px;top:398px">HALFBACK STEAK</div><div class="abs dprice" style="left:797px;top:398px">$ 28</div><div class="abs dprice" style="left:865px;top:398px">$30</div>
    <div class="desc desc-l" style="top:412px">Huge rump steak topped with fanned avocado,<br>melted cheese &amp; button mushroom sauce</div>

    <div class="abs dish" style="left:618px;top:452px">THE FULL HOUSE</div><div class="abs dprice" style="left:797px;top:452px">$ 28</div><div class="abs dprice" style="left:865px;top:452px">$30</div>
    <div class="desc desc-l" style="top:466px">A massive T-bone steak topped with a special sea-<br>food mix of prawns, calamari, mussels, scallops<br>etc. with a spicy tomato &amp; basil sauce</div>

    <div class="abs dish" style="left:618px;top:519px">CATTLEMANS STEAK</div><div class="abs dprice" style="left:797px;top:519px">$ 28</div><div class="abs dprice" style="left:865px;top:519px">$30</div>
    <div class="desc desc-l" style="top:534px">350g rib eye steak on the bone</div>

    <div class="abs dish" style="left:618px;top:560px">BBQ AMERICAN PORK RIBS</div><div class="abs dprice" style="left:797px;top:560px">$ 28</div><div class="abs dprice" style="left:865px;top:560px">$30</div>
    <div class="desc desc-l" style="top:574px">Hickory smoked pork ribs, roasted in a BBQ sauce</div>

    <div class="abs dish" style="left:618px;top:603px">RIB COMBO 1</div><div class="abs dprice" style="left:797px;top:603px">$ 28</div><div class="abs dprice" style="left:865px;top:603px">$30</div>
    <div class="desc desc-l" style="top:617px">Hickory smoked pork ribs, with char grilled chick-<br>en breast</div>

    <div class="abs dish" style="left:618px;top:656px">RIB COMBO 2</div><div class="abs dprice" style="left:797px;top:656px">$ 28</div><div class="abs dprice" style="left:865px;top:656px">$30</div>
    <div class="desc desc-l" style="top:670px">Hickory smoked pork ribs, with char grilled rump<br>steak</div>

    <div class="abs col-head" style="left:1073px;top:141px;letter-spacing:1px">MEMBER</div>
    <div class="abs col-head" style="left:1142px;top:141px;letter-spacing:1px">VISITOR</div>
    <div class="abs dish" style="left:910px;top:153px">VEAL OR CHICKEN SCHNITZEL</div><div class="abs dprice" style="left:1087px;top:153px">$ 20</div><div class="abs dprice" style="left:1157px;top:153px">$22</div>
    <div class="abs dish" style="left:910px;top:172px">MIXED GRILL</div><div class="abs dprice" style="left:1087px;top:172px">$ 20</div><div class="abs dprice" style="left:1157px;top:172px">$22</div>
    <div class="abs dish" style="left:910px;top:191px">RUMP STEAK 200g</div><div class="abs dprice" style="left:1087px;top:191px">$ 20</div><div class="abs dprice" style="left:1157px;top:191px">$22</div>
    <div class="abs dish" style="left:910px;top:210px">RUMP STEAK 400g</div><div class="abs dprice" style="left:1087px;top:210px">$ 27</div><div class="abs dprice" style="left:1157px;top:210px">$29</div>
    <div class="abs dish" style="left:910px;top:229px">T-BONE 400g</div><div class="abs dprice" style="left:1087px;top:229px">$ 27</div><div class="abs dprice" style="left:1157px;top:229px">$29</div>
    <div class="abs dish" style="left:910px;top:248px">RIB FILLET 350g</div><div class="abs dprice" style="left:1087px;top:248px">$ 27</div><div class="abs dprice" style="left:1157px;top:248px">$29</div>

    <div class="abs sec" style="left:910px;top:276px;width:270px">VEAL</div>
    <div class="abs dish" style="left:910px;top:297px">VEAL ala FUNGI</div><div class="abs dprice" style="left:1087px;top:297px">$ 22</div><div class="abs dprice" style="left:1157px;top:297px">$24</div>
    <div class="desc desc-r" style="top:311px">Succulent pan fried veal, in a creamy mushroom<br>sauce</div>
    <div class="abs dish" style="left:910px;top:344px">VEAL DIANE</div><div class="abs dprice" style="left:1087px;top:344px">$ 22</div><div class="abs dprice" style="left:1157px;top:344px">$24</div>
    <div class="desc desc-r" style="top:358px">Tender scallops of pan fried veal with a smooth<br>creamy diane sauce</div>

    <div class="abs sec" style="left:910px;top:402px;width:270px">LAMB</div>
    <div class="abs dish" style="left:910px;top:421px">CRUMBED LAMB CUTLETS</div><div class="abs dprice" style="left:1100px;top:421px">$ 25</div><div class="abs dprice" style="left:1160px;top:421px">$27</div>

    <div class="abs sec" style="left:910px;top:449px;width:270px">CHICKEN</div>
    <div class="abs dish" style="left:910px;top:468px">SPECIAL NUMBER 1</div><div class="abs dprice" style="left:1100px;top:468px">$ 25</div><div class="abs dprice" style="left:1160px;top:468px">$27</div>
    <div class="desc desc-r" style="top:482px">Breast of grilled chicken served with a prawn,<br>bacon, onion &amp; avocado garlic cream sauce</div>
    <div class="abs dish" style="left:910px;top:517px">GARLIC CHICKEN &amp; PRAWN</div><div class="abs dprice" style="left:1100px;top:517px">$ 25</div><div class="abs dprice" style="left:1160px;top:517px">$27</div>
    <div class="desc desc-r" style="top:531px">Grilled breast of chicken topped with a creamy<br>garlic sauce &amp; king prawns</div>
    <div class="abs dish" style="left:910px;top:565px">CHICKEN SCALOPPINE</div><div class="abs dprice" style="left:1100px;top:565px">$ 25</div><div class="abs dprice" style="left:1160px;top:565px">$27</div>
    <div class="desc desc-r" style="top:579px">Pan fried breast of chicken with a bacon, onion,<br>mushroom, parsley, garlic &amp; parmesan cream<br>sauce</div>
    <div class="abs dish" style="left:910px;top:626px">CHICKEN &amp; ASPARAGUS</div><div class="abs dprice" style="left:1100px;top:626px">$ 25</div><div class="abs dprice" style="left:1160px;top:626px">$27</div>
    <div class="desc desc-r" style="top:640px">Succulent grilled breast of chicken with garlic, as-<br>paragus &amp; Bearnaise sauce</div>
    <div class="abs dish" style="left:910px;top:674px">CHICKEN PARMIGANA</div><div class="abs dprice" style="left:1100px;top:674px">$ 25</div><div class="abs dprice" style="left:1160px;top:674px">$27</div>
    <div class="desc desc-r" style="top:688px">Crumbed breast of chicken topped with tomato<br>basil sauce, Finished with our own cheese mix</div>

    <div class="abs footnote" style="left:600px;top:789px;width:588px;text-align:center">All main meals are served with chips &amp; salad or mashed potato &amp; vegetables</div>
  </div>
</div>
</body>
</html>
```